Little Meadow Press Website

We need a wordpress design for a new independent children's book publishers based in Oxford in the UK. The design should be fun and colourful. I have supplied an example template of some of the text/images but open to other ideas.
The design should communicate that Little Meadow Press are producers of fun and interactive children's illustrated books.

Target Market(s)

Booksellers, International

```html
<!DOCTYPE html>
<html lang="en">
<head>
<meta charset="utf-8">
<title>Little Meadow Press</title>
<link href="https://fonts.googleapis.com/css2?family=Cinzel:wght@400;700&family=Gochi+Hand&family=Open+Sans:wght@400;600&display=swap" rel="stylesheet">
<style>
:root{
  --orange:#f26a1b;
  --yellow:#fdc20f;
  --green:#4db81a;
  --sky:#2e8ed0;
  --sky-light:#3d9ad8;
  --red:#ee2430;
  --white:#ffffff;
  --ink:#555b60;
}
*{margin:0;padding:0;box-sizing:border-box}
html,body{width:820px;height:1200px;overflow:hidden;background:var(--white)}
body{position:relative;font-family:"Open Sans",Arial,sans-serif}
.rainbow-strip{position:absolute;top:0;left:0;width:820px;height:3px;
  background:linear-gradient(90deg,var(--red) 0 12%,var(--orange) 12% 24%,var(--yellow) 24% 36%,var(--green) 36% 48%,var(--sky) 48% 60%,#8b5cc7 60% 72%,var(--red) 72% 84%,#2b3f8f 84% 100%)}
.site-header{position:absolute;top:3px;left:0;width:820px;height:93px}
.brand{position:absolute;left:67px;top:34px;display:flex;align-items:center;gap:8px;
  font-family:"Cinzel",serif;font-weight:700;font-size:16px;color:var(--sky)}
.brand-dot{width:14px;height:14px;border-radius:50%;background:var(--yellow)}
.main-nav{position:absolute;left:427px;top:16px;display:flex;height:62px}
.main-nav a{display:flex;align-items:center;justify-content:center;text-align:center;
  font-family:"Cinzel",serif;font-size:9.5px;color:var(--white);text-decoration:none;line-height:1.5;position:relative}
.nav-home{width:59px;background:var(--orange)}
.nav-home::after{content:"";position:absolute;bottom:-6px;left:50%;margin-left:-5px;
  border-left:5px solid transparent;border-right:5px solid transparent;border-top:6px solid var(--orange)}
.nav-about{width:59px;background:var(--yellow)}
.nav-books{width:59px;background:var(--green)}
.nav-authors{width:83px;background:var(--sky-light)}
.nav-contact{width:65px;background:var(--red)}
.hero{position:absolute;top:96px;left:0;width:820px;height:438px;
  background:radial-gradient(ellipse at 50% 0%,#4aa3e0 0%,var(--sky) 55%)}
.hero svg{position:absolute;left:0;top:0}
.hero-slogan{position:absolute;left:108px;top:128px;font-family:"Gochi Hand",cursive;font-size:58px;line-height:62px}
.hero-slogan span{display:inline-block;margin-right:2px}
.w-blue{color:#4fb1ee}.w-yellow{color:var(--yellow)}.w-green{color:#8bd12a}.w-red{color:var(--red)}.w-orange{color:var(--orange)}
.slider-dots{position:absolute;top:343px;left:368px;display:flex;gap:5px}
.slider-dots span{width:25px;height:25px;border-radius:50%;background:#e4e4e4;border:2px solid var(--white);
  font-family:"Gochi Hand",cursive;font-size:15px;color:#555;display:flex;align-items:center;justify-content:center}
.slider-dots .active{background:#333;color:var(--white)}
.welcome{position:absolute;top:534px;left:0;width:820px;height:289px;background:var(--yellow)}
.welcome h2{position:absolute;left:67px;top:20px;font-family:"Gochi Hand",cursive;font-weight:400;font-size:36px;color:var(--white)}
.welcome p{position:absolute;left:67px;top:80px;width:230px;font-size:10.5px;line-height:16.4px;color:var(--white)}
.btn{position:absolute;width:80px;height:32px;display:flex;align-items:center;justify-content:center;
  font-family:"Gochi Hand",cursive;font-size:15px;color:var(--white);text-decoration:none}
.btn-red{background:var(--red);left:67px;top:228px}
.btn-green{background:var(--green);left:67px;top:204px}
.book-card{position:absolute;top:43px;width:190px;height:205px}
.book-card svg{position:absolute;left:0;top:0}
.book-card .card-title{position:absolute;left:0;top:160px;width:190px;text-align:center;
  font-family:"Gochi Hand",cursive;font-size:21px;color:var(--white)}
.card-badger{left:342px}
.card-rosie{left:562px}
.audience{position:absolute;top:823px;left:0;width:820px;height:257px;background:var(--white)}
.audience-photo{position:absolute;left:487px;top:0;width:305px;height:257px;z-index:0;
  background:linear-gradient(180deg,#f7f3f2 0%,#e8b8c8 45%,#8a9ab8 80%,#f2f2f2 100%)}
.audience h2{position:absolute;z-index:1;left:67px;top:22px;width:420px;font-family:"Gochi Hand",cursive;font-weight:400;
  font-size:34px;line-height:34px;color:var(--sky)}
.audience .lead{position:absolute;z-index:1;left:67px;top:105px;width:415px;font-size:15px;line-height:19px;color:var(--red)}
.audience .body-copy{position:absolute;z-index:1;left:67px;top:160px;width:410px;font-size:9.5px;line-height:15px;color:var(--ink)}
.site-footer{position:absolute;top:1080px;left:0;width:820px;height:120px;background:var(--red)}
.social{position:absolute;left:66px;top:14px;display:flex;gap:4px}
.social span{width:40px;height:40px;border-radius:50%;border:2px solid var(--white)}
.social .s1{background:#1d9be6}.social .s2{background:#2e4a8a}.social .s3{background:#2a7bc0}
.footer-nav{position:absolute;left:68px;top:72px;font-family:"Cinzel",serif;font-size:10px;color:var(--white)}
.footer-nav a{color:var(--white);text-decoration:none}
.footer-nav i{font-style:normal;margin:0 5px}
.copyright{position:absolute;left:67px;top:93px;font-family:"Cinzel",serif;font-size:7.5px;color:var(--white)}
.footer-brand{position:absolute;left:607px;top:84px;display:flex;align-items:center;gap:6px;
  font-family:"Cinzel",serif;font-weight:700;font-size:13px;color:#f7c9a0}
.footer-brand .brand-dot{width:11px;height:11px;background:#f7c9a0}
</style>
</head>
<body>
<div class="rainbow-strip"></div>

<header class="site-header">
  <div class="brand"><span class="brand-dot"></span>Little Meadow Press</div>
  <nav class="main-nav">
    <a class="nav-home" href="#">HOME</a>
    <a class="nav-about" href="#">ABOUT</a>
    <a class="nav-books" href="#">BOOKS</a>
    <a class="nav-authors" href="#">AUTHORS<br>ILLUSTRATORS</a>
    <a class="nav-contact" href="#">CONTACT<br>US</a>
  </nav>
</header>

<section class="hero">
  <svg width="820" height="438" viewBox="0 0 820 438">
    <defs>
      <linearGradient id="heroPhoto" x1="0" y1="0" x2="0" y2="1">
        <stop offset="0" stop-color="#3f5a2a"/>
        <stop offset="0.5" stop-color="#7f9a4a"/>
        <stop offset="1" stop-color="#5d8a2c"/>
      </linearGradient>
    </defs>
    <path d="M67 45 H752 V346 Q410 430 67 346 Z" fill="#ffffff"/>
    <path role="img" aria-label="Photo of a young girl reading a book on the grass" d="M73 51 H747 V340 Q410 418 73 340 Z" fill="url(#heroPhoto)"/>
  </svg>
  <div class="hero-slogan">
    <div><span class="w-blue">Bright</span><span class="w-yellow">Book</span><span class="w-green">For</span></div>
    <div><span class="w-red">Bright</span><span class="w-orange">Minds</span></div>
  </div>
  <div class="slider-dots"><span class="active">1</span><span>2</span><span>3</span></div>
</section>

<section class="welcome">
  <h2>Welcome!</h2>
  <p>Little Meadow Press is a new independent publishing company publishing inspiring and quality children's illustrated books. Our aim is to print stories that are not only entertain-ing, but encourage and inspire children to explore different activities and aspects of life, as shown by our first two titles 'The Badger Bakery' and 'Captain Rosie'</p>
  <a class="btn btn-red" href="#">Read More</a>

  <article class="book-card card-badger">
    <svg width="190" height="205" viewBox="0 0 190 205">
      <path d="M0 20 Q95 -8 190 20 V188 Q95 214 0 188 Z" fill="#2e8ed0"/>
      <path role="img" aria-label="Photo of two children reading a picture book together" d="M0 20 Q95 -8 190 20 V156 H0 Z" fill="#c9d8e0"/>
    </svg>
    <div class="card-title">The Badger Bakery</div>
  </article>

  <article class="book-card card-rosie">
    <svg width="190" height="205" viewBox="0 0 190 205">
      <path d="M0 20 Q95 -8 190 20 V188 Q95 214 0 188 Z" fill="#4db81a"/>
      <path role="img" aria-label="Photo of two little girls looking at a book" d="M0 20 Q95 -8 190 20 V156 H0 Z" fill="#d8c8c4"/>
    </svg>
    <div class="card-title">Captain Rosie</div>
  </article>
</section>

<section class="audience">
  <div class="audience-photo" role="img" aria-label="Photo of a toddler in a pink jumper reading a book"></div>
  <h2>Our books are aimed at one to five year old</h2>
  <p class="lead">and we are looking for new talent as well as established authors and illustrators.</p>
  <p class="body-copy">Lorem ipsum dolor sit amet conse ctetur adipisicing elit, sed do eiusmod tempor incididunt ut labore et dolore magna aliqua. Ut enim ad minim veniam, quis nostrud exercitation.</p>
  <a class="btn btn-green" href="#">Read More</a>
</section>

<footer class="site-footer">
  <div class="social" role="img" aria-label="Social media links"><span class="s1"></span><span class="s2"></span><span class="s3"></span></div>
  <nav class="footer-nav"><a href="#">HOME</a><i>|</i><a href="#">ABOUT</a><i>|</i><a href="#">BOOKS</a><i>|</i><a href="#">AUTHORS / ILLUSTRATORS</a><i>|</i><a href="#">CONTACT US</a></nav>
  <div class="copyright">LITTLE MEADOW PRESS © 2015 ALL RIGHTS RESERVED PRIVACY POLICY</div>
  <div class="footer-brand"><span class="brand-dot"></span>Little Meadow Press</div>
</footer>
</body>
</html>
```